Redesign of iOS App Moriva Tutor

Redesign of existing App Moriva Tutor, an app that helps learning Japanese Kanjis, Hiragana, Katakana.

The functionallity should remain the same as today: the app is free, you may download it at the app store. But: I like the design of my other apps better ;)

Target Market(s)

Students learning Japanese

Industry/Entity Type

Teacher

Font styles to use
Sans Serif

Requirements
Must have
• Moriva Tutor has 7 main screens, all screens has to be designed for iPhone and iPad: Main, Settings, Reading Tests, Writing Tests, Game, Paper Mode, Search
Nice to have
• I like the logo as it is today

```html
<!DOCTYPE html>
<html lang="en">
<head>
<meta charset="utf-8">
<title>Moriva Tutor — App Redesign</title>
<link href="https://fonts.googleapis.com/css2?family=Roboto:wght@400;500&family=Noto+Sans+JP:wght@300;400&display=swap" rel="stylesheet">
<style>
:root{
  --page:#3f3f3f;
  --white:#ffffff;
  --ink:#2b2b2b;
  --muted:#8a8a8a;
  --line:#e6e6e6;
  --tile:#efefef;
  --tile-border:#d9d9d9;
  --dark:#3a3a3a;
  --red:#f15a48;
  --teal:#17c3b0;
  --blue:#3e97ee;
  --yellow:#f3b23a;
  --tab:#f7f7f7;
  --tab-active:#8a8a8a;
  --dim:rgba(30,30,30,.72);
}
*{box-sizing:border-box;margin:0;padding:0}
html,body{width:1200px;height:1200px;overflow:hidden;background:var(--page)}
body{position:relative;font-family:'Roboto',Helvetica,Arial,sans-serif;color:var(--ink)}
.jp{font-family:'Noto Sans JP','Roboto',sans-serif}

.phone{position:absolute;width:315px;height:559px;background:var(--white);overflow:hidden}
.status{position:absolute;top:0;left:0;right:0;height:16px;font-size:8px;color:#444;display:flex;align-items:center;padding:0 6px}
.status .carrier{flex:1}
.status .time{position:absolute;left:0;right:0;text-align:center}
.status .battery{flex:1;text-align:right}
.status .batt{display:inline-block;width:18px;height:7px;background:#444;vertical-align:middle;margin-left:3px;border-radius:1px}
.navbar{position:absolute;top:16px;left:0;right:0;height:36px;border-bottom:1px solid var(--line);display:flex;align-items:center;justify-content:center;font-size:12px;letter-spacing:.3px}
.navbar .back{position:absolute;left:14px;top:10px}

.stats{position:absolute;top:52px;left:0;right:0;height:60px;display:flex;justify-content:space-around;align-items:center;padding:0 24px;border-bottom:6px solid #f4f4f4}
.stat{width:46px;height:46px;border-radius:50%;color:#fff;display:flex;flex-direction:column;align-items:center;justify-content:center;box-shadow:0 1px 2px rgba(0,0,0,.3)}
.stat b{font-weight:400;font-size:14px;line-height:14px}
.stat small{font-size:5.5px;margin-top:2px}
.stat.dark{background:var(--dark)}.stat.red{background:var(--red)}.stat.teal{background:var(--teal)}.stat.blue{background:var(--blue)}.stat.yellow{background:var(--yellow)}

.prompt{position:absolute;top:112px;left:0;right:0;height:68px;border-bottom:1px solid var(--line);text-align:center}
.prompt .word{font-size:28px;line-height:44px;margin-top:4px}
.prompt .reading{font-size:10px;color:var(--muted)}
.prompt .fav{position:absolute;right:14px;top:18px}
.prompt.short{height:52px}
.prompt.short .word{font-size:17px;line-height:22px;margin-top:12px}

.tile{position:absolute;width:86px;height:86px;background:var(--tile);border:1px solid var(--tile-border);border-radius:2px;display:flex;align-items:center;justify-content:center;font-size:13.5px}
.tile.kana{font-size:22px;font-family:'Noto Sans JP',sans-serif}
.tile.right{background:var(--teal);border-color:var(--teal);color:#fff}
.tile.wrong{background:var(--red);border-color:var(--red);color:#fff}
.c1{left:13px}.c2{left:114px}.c3{left:216px}
.r1{top:197px}.r2{top:301px}.r3{top:405px}

.skip{position:absolute;right:22px;top:524px;font-size:16px;color:#777}

.tabbar{position:absolute;bottom:0;left:0;right:0;height:40px;background:var(--tab);border-top:1px solid #ddd;display:flex}
.tabbar .tab{flex:1;display:flex;flex-direction:column;align-items:center;justify-content:center;font-size:5.5px;color:#666;border-right:1px solid #e2e2e2}
.tabbar .tab svg{width:20px;height:20px;margin-bottom:1px}
.tabbar .tab.on{background:var(--tab-active);color:#fff}

.dimmer{position:absolute;inset:0;background:var(--dim)}
.dialog{position:absolute;left:10px;top:214px;width:294px;height:150px;background:#fff;border-radius:3px;box-shadow:0 2px 10px rgba(0,0,0,.4);overflow:hidden}
.dialog p{height:112px;display:flex;align-items:center;justify-content:center;text-align:center;font-size:17px;line-height:21px;color:#333;padding:0 44px}
.dialog .actions{position:absolute;bottom:0;left:0;right:0;height:38px;background:#f6f6f6;display:flex}
.dialog .actions span{flex:1;text-align:center;line-height:38px;font-size:17px}
.no{color:var(--red)}.yes{color:var(--teal)}

/* search */
.searchbar{position:absolute;top:52px;left:0;right:0;height:32px;border-bottom:1px solid var(--line);display:flex;align-items:center;padding-left:20px;font-size:11px;color:var(--muted)}
.searchbar svg{margin-right:14px}
.found{position:absolute;right:14px;top:10px;background:#8c8c8c;color:#fff;font-size:7.5px;padding:4px 15px;border-radius:9px}
.row{position:absolute;left:0;right:0;height:56px;border-left:4px solid #8a8a8a;border-bottom:2px solid #f2f2f2;display:flex;align-items:center;font-size:10.5px;color:var(--muted)}
.row .kana{width:52px;padding-left:10px;font-size:25px;color:var(--ink);font-family:'Noto Sans JP',sans-serif;font-weight:300}
.row .rom{width:62px}
.row .type{width:118px}
.row .k{width:50px}
.row.blue{border-left-color:var(--blue)}.row.red{border-left-color:var(--red)}
.popover{position:absolute;left:153px;top:58px;width:157px;height:117px;background:#fff;border:1px solid #ccc;border-radius:3px;box-shadow:0 2px 6px rgba(0,0,0,.2);text-align:center;font-size:7.5px;color:#444}
.popover .pill{margin:12px 10px 4px;background:var(--dark);color:#fff;font-size:10px;line-height:16px;border-radius:8px}
.popover .label{border-top:1px solid #ddd;margin:0 8px;padding-top:5px}
.dots{display:flex;justify-content:space-around;padding:6px 14px 8px}
.dots i{width:16px;height:16px;border-radius:50%;display:block}
.stars{display:flex;justify-content:center;gap:24px;padding-top:4px}

/* game */
.powerups{position:absolute;left:14px;top:479px;width:288px;height:29px;background:var(--yellow);border-radius:15px;display:flex;align-items:center;padding:0 6px 0 22px;gap:6px;color:#fff;font-size:5.5px}
.powerups .item{display:flex;align-items:center;gap:3px;width:55px}
.powerups .item.off{opacity:.45}
.powerups .end{margin-left:auto;width:22px;height:22px;border-radius:50%;background:#fff;display:flex;align-items:center;justify-content:center}

/* paper */
.canvas-area{position:absolute;top:164px;left:0;right:0;height:314px;border-bottom:1px solid var(--line)}
.canvas-area .v{position:absolute;left:156px;top:0;bottom:0;width:1px;background:#eee}
.canvas-area .h{position:absolute;top:157px;left:0;right:0;height:1px;background:#eee}
.guide{position:absolute;inset:0;display:flex;align-items:center;justify-content:center;font-family:'Noto Sans JP',sans-serif;font-weight:300;font-size:280px;color:#e4e4e4;line-height:1}

.brand{position:absolute;left:1030px;top:556px;width:160px;text-align:center;color:#fff;font-size:24px;font-weight:500;line-height:1.2}
</style>
</head>
<body>

<svg width="0" height="0" style="position:absolute">
  <defs>
    <symbol id="i-home" viewBox="0 0 24 24"><path d="M3 11 12 3l9 8M5 9v12h5v-6h4v6h5V9" fill="none" stroke="currentColor" stroke-width="1.3"/></symbol>
    <symbol id="i-gear" viewBox="0 0 24 24"><circle cx="12" cy="12" r="3.5" fill="none" stroke="currentColor" stroke-width="1.3"/><path d="M12 2v3M12 19v3M2 12h3M19 12h3M4.9 4.9l2.1 2.1M17 17l2.1 2.1M4.9 19.1 7 17M17 7l2.1-2.1" stroke="currentColor" stroke-width="1.3"/><circle cx="12" cy="12" r="7" fill="none" stroke="currentColor" stroke-width="1.3"/></symbol>
    <symbol id="i-search" viewBox="0 0 24 24"><circle cx="10" cy="10" r="7" fill="none" stroke="currentColor" stroke-width="1.4"/><path d="m15 15 7 7" stroke="currentColor" stroke-width="1.4"/></symbol>
    <symbol id="i-grid" viewBox="0 0 24 24"><g fill="none" stroke="currentColor" stroke-width="1.2"><rect x="2" y="2" width="5.5" height="5.5"/><rect x="9.3" y="2" width="5.5" height="5.5"/><rect x="16.5" y="2" width="5.5" height="5.5"/><rect x="2" y="9.3" width="5.5" height="5.5"/><rect x="9.3" y="9.3" width="5.5" height="5.5"/><rect x="16.5" y="9.3" width="5.5" height="5.5"/><rect x="2" y="16.5" width="5.5" height="5.5"/><rect x="9.3" y="16.5" width="5.5" height="5.5"/><rect x="16.5" y="16.5" width="5.5" height="5.5"/></g></symbol>
    <symbol id="i-paper" viewBox="0 0 24 24"><rect x="4" y="2" width="16" height="20" fill="none" stroke="currentColor" stroke-width="1.3"/><path d="M8 8h8M8 12h8M8 16h8" stroke="currentColor" stroke-width="1.3"/></symbol>
    <symbol id="i-star" viewBox="0 0 24 24"><path d="m12 2 2.9 6.6 7.1.6-5.4 4.7 1.6 7-6.2-3.7-6.2 3.7 1.6-7L2 9.2l7.1-.6z"/></symbol>
    <symbol id="i-star-o" viewBox="0 0 24 24"><path d="m12 2 2.9 6.6 7.1.6-5.4 4.7 1.6 7-6.2-3.7-6.2 3.7 1.6-7L2 9.2l7.1-.6z" fill="none" stroke="currentColor" stroke-width="1.6"/></symbol>
    <symbol id="i-back" viewBox="0 0 24 24"><path d="M15 3 6 12l9 9" fill="none" stroke="currentColor" stroke-width="2"/></symbol>
  </defs>
</svg>

<!-- Search screen -->
<section class="phone" style="left:30px;top:32px">
  <div class="status"><span class="carrier">●●●●● Kestrel</span><span class="time">9:41 AM</span><span class="battery">100%<i class="batt"></i></span></div>
  <div class="navbar">SEARCH<span class="found">2278 Found</span></div>
  <div class="searchbar"><svg width="12" height="12"><use href="#i-search"/></svg>Type here for search</div>
  <div class="row blue" style="top:94px"><span class="kana">あ</span><span class="rom">a</span><span class="type">Hiragana</span><span class="k">K</span><svg width="13" height="13" color="#333"><use href="#i-star-o"/></svg></div>
  <div class="row red" style="top:152px"><span class="kana">い</span><span class="rom">i</span><span class="type">Hiragana</span><span class="k">K</span><svg width="13" height="13" color="#333"><use href="#i-star-o"/></svg></div>
  <div class="row" style="top:210px"><span class="kana">う</span><span class="rom">u</span><span class="type">Hiragana</span><span class="k">K</span><svg width="13" height="13" color="#333"><use href="#i-star-o"/></svg></div>
  <div class="row" style="top:268px"><span class="kana">え</span><span class="rom">e</span><span class="type">Hiragana</span><span class="k">K</span><svg width="13" height="13" color="#333"><use href="#i-star-o"/></svg></div>
  <div class="row" style="top:326px"><span class="kana">お</span><span class="rom">o</span><span class="type">Hiragana</span><span class="k">K</span><svg width="13" height="13" color="#333"><use href="#i-star-o"/></svg></div>
  <div class="row" style="top:384px"><span class="kana">か</span><span class="rom">ka</span><span class="type">Hiragana</span><span class="k">K</span><svg width="13" height="13" color="#333"><use href="#i-star-o"/></svg></div>
  <div class="row" style="top:442px"><span class="kana">が</span><span class="rom">ga</span><span class="type">Hiragana</span><span class="k">K</span><svg width="13" height="13" color="#333"><use href="#i-star-o"/></svg></div>
  <div class="row" style="top:500px"></div>
  <div class="popover">
    <div class="pill">Practice Writing</div>
    <div class="label">Mark 30848 Tests</div>
    <div class="dots"><i style="background:#9a9a9a"></i><i style="background:var(--red)"></i><i style="background:var(--blue)"></i><i style="background:var(--teal)"></i></div>
    <div class="label">Mark 2136 Kanjis</div>
    <div class="stars"><svg width="14" height="14"><use href="#i-star"/></svg><svg width="14" height="14" color="#333"><use href="#i-star-o"/></svg></div>
  </div>
  <nav class="tabbar">
    <div class="tab"><svg><use href="#i-home"/></svg>Home</div>
    <div class="tab"><svg><use href="#i-gear"/></svg>Settings</div>
    <div class="tab on"><svg><use href="#i-search"/></svg>Search</div>
    <div class="tab"><svg><use href="#i-grid"/></svg>Game</div>
    <div class="tab"><svg><use href="#i-paper"/></svg>Paper</div>
  </nav>
</section>

<!-- Kanji meaning test -->
<section class="phone" style="left:366px;top:32px">
  <div class="status"><span class="carrier">●●●●● Kestrel</span><span class="time">9:41 AM</span><span class="battery">100%<i class="batt"></i></span></div>
  <div class="navbar"><svg class="back" width="14" height="16"><use href="#i-back"/></svg>KANJI - MEANING</div>
  <div class="stats"><div class="stat dark"><b>107</b><small>Remain</small></div><div class="stat red"><b>2</b><small>Wrong</small></div><div class="stat teal"><b>10</b><small>Correct</small></div></div>
  <div class="prompt"><div class="word jp">名</div><div class="reading jp">メイ, ミョウ, な</div><svg class="fav" width="15" height="15"><use href="#i-star"/></svg></div>
  <div class="tile c1 r1">Seven</div><div class="tile c2 r1">Person</div><div class="tile c3 r1">Long</div>
  <div class="tile c1 r2 right">Name</div><div class="tile c2 r2">Come</div><div class="tile c3 r2">Many</div>
  <div class="tile c1 r3">Write</div><div class="tile c2 r3">In</div><div class="tile c3 r3 wrong">Station</div>
  <div class="skip">Skip »</div>
</section>

<!-- Kanji meaning test — cancel dialog -->
<section class="phone" style="left:701px;top:32px">
  <div class="status"><span class="carrier">●●●●● Kestrel</span><span class="time">9:41 AM</span><span class="battery">100%<i class="batt"></i></span></div>
  <div class="navbar"><svg class="back" width="14" height="16"><use href="#i-back"/></svg>KANJI - MEANING</div>
  <div class="stats"><div class="stat dark"><b>107</b><small>Remain</small></div><div class="stat red"><b>2</b><small>Wrong</small></div><div class="stat teal"><b>10</b><small>Correct</small></div></div>
  <div class="prompt"><div class="word jp">名</div><div class="reading jp">メイ, ミョウ, な</div><svg class="fav" width="15" height="15"><use href="#i-star"/></svg></div>
  <div class="tile c1 r1">Seven</div><div class="tile c2 r1">Person</div><div class="tile c3 r1">Long</div>
  <div class="tile c1 r2 right">Name</div><div class="tile c2 r2">Come</div><div class="tile c3 r2">Many</div>
  <div class="tile c1 r3">Write</div><div class="tile c2 r3">In</div><div class="tile c3 r3 wrong">Station</div>
  <div class="skip">Skip »</div>
  <div class="dimmer"></div>
  <div class="dialog"><p>Are you sure you want to cancel the test ?</p><div class="actions"><span class="no">No</span><span class="yes">Yes</span></div></div>
</section>

<!-- Game -->
<section class="phone" style="left:30px;top:612px">
  <div class="status"><span class="carrier">●●●●● Kestrel</span><span class="time">9:41 AM</span><span class="battery">100%<i class="batt"></i></span></div>
  <div class="navbar">GAME</div>
  <div class="stats"><div class="stat red"><b>3</b><small>Lives</small></div><div class="stat blue"><b>0</b><small>Score</small></div><div class="stat yellow"><b>10</b><small>Coins</small></div></div>
  <div class="prompt short"><div class="word">GO</div><svg class="fav" width="15" height="15"><use href="#i-star"/></svg></div>
  <div class="tile kana c1" style="top:177px">そ</div><div class="tile kana c2" style="top:177px">ご</div><div class="tile kana c3" style="top:177px">あ</div>
  <div class="tile kana c1" style="top:278px">ぽ</div><div class="tile kana c2" style="top:278px">ふ</div><div class="tile kana c3" style="top:278px">む</div>
  <div class="tile kana c1" style="top:379px">う</div><div class="tile kana c2" style="top:379px">せ</div><div class="tile kana c3" style="top:379px">た</div>
  <div class="powerups">
    <div class="item"><svg width="10" height="14" viewBox="0 0 10 14"><path d="M5 0 10 6H7v8H3V6H0z" fill="#fff"/></svg>Level<br>Up</div>
    <div class="item off"><svg width="14" height="12" viewBox="0 0 24 22"><path d="M12 21 2 11a5.5 5.5 0 0 1 10-7 5.5 5.5 0 0 1 10 7z" fill="#fff"/></svg>Lives+<br>-24</div>
    <div class="item"><svg width="12" height="14" viewBox="0 0 12 14"><path d="M6 14V7L1 2M6 7l5-5M0 0h3M9 0h3" stroke="#fff" stroke-width="2" fill="none"/></svg>Split<br>-8</div>
    <div class="item off"><svg width="10" height="14" viewBox="0 0 10 14"><circle cx="5" cy="5" r="5" fill="#fff"/><rect x="3" y="10" width="4" height="4" fill="#fff"/></svg>Hint<br>-4</div>
    <div class="end"><svg width="10" height="10" viewBox="0 0 10 10"><path d="M8 0v10L0 5z" fill="var(--yellow)"/></svg></div>
  </div>
  <nav class="tabbar">
    <div class="tab"><svg><use href="#i-home"/></svg>Home</div>
    <div class="tab"><svg><use href="#i-gear"/></svg>Settings</div>
    <div class="tab"><svg><use href="#i-search"/></svg>Search</div>
    <div class="tab on"><svg><use href="#i-grid"/></svg>Game</div>
    <div class="tab"><svg><use href="#i-paper"/></svg>Paper</div>
  </nav>
</section>

<!-- Game — cancel dialog -->
<section class="phone" style="left:366px;top:612px">
  <div class="status"><span class="carrier">●●●●● Kestrel</span><span class="time">9:41 AM</span><span class="battery">100%<i class="batt"></i></span></div>
  <div class="navbar">GAME</div>
  <div class="stats"><div class="stat red"><b>3</b><small>Lives</small></div><div class="stat blue"><b>0</b><small>Score</small></div><div class="stat yellow"><b>10</b><small>Coins</small></div></div>
  <div class="prompt short"><div class="word">GO</div><svg class="fav" width="15" height="15"><use href="#i-star"/></svg></div>
  <div class="tile kana c1" style="top:177px">そ</div><div class="tile kana c2" style="top:177px">ご</div><div class="tile kana c3" style="top:177px">あ</div>
  <div class="tile kana c1" style="top:278px">ぽ</div><div class="tile kana c2" style="top:278px">ふ</div><div class="tile kana c3" style="top:278px">む</div>
  <div class="tile kana c1" style="top:379px">う</div><div class="tile kana c2" style="top:379px">せ</div><div class="tile kana c3" style="top:379px">た</div>
  <div class="powerups">
    <div class="item"><svg width="10" height="14" viewBox="0 0 10 14"><path d="M5 0 10 6H7v8H3V6H0z" fill="#fff"/></svg>Level<br>Up</div>
    <div class="item off"><svg width="14" height="12" viewBox="0 0 24 22"><path d="M12 21 2 11a5.5 5.5 0 0 1 10-7 5.5 5.5 0 0 1 10 7z" fill="#fff"/></svg>Lives+<br>-24</div>
    <div class="item"><svg width="12" height="14" viewBox="0 0 12 14"><path d="M6 14V7L1 2M6 7l5-5M0 0h3M9 0h3" stroke="#fff" stroke-width="2" fill="none"/></svg>Split<br>-8</div>
    <div class="item off"><svg width="10" height="14" viewBox="0 0 10 14"><circle cx="5" cy="5" r="5" fill="#fff"/><rect x="3" y="10" width="4" height="4" fill="#fff"/></svg>Hint<br>-4</div>
    <div class="end"><svg width="10" height="10" viewBox="0 0 10 10"><path d="M8 0v10L0 5z" fill="var(--yellow)"/></svg></div>
  </div>
  <nav class="tabbar">
    <div class="tab"><svg><use href="#i-home"/></svg>Home</div>
    <div class="tab"><svg><use href="#i-gear"/></svg>Settings</div>
    <div class="tab"><svg><use href="#i-search"/></svg>Search</div>
    <div class="tab on"><svg><use href="#i-grid"/></svg>Game</div>
    <div class="tab"><svg><use href="#i-paper"/></svg>Paper</div>
  </nav>
  <div class="dimmer"></div>
  <div class="dialog"><p>Are you sure you want to cancel the Game?</p><div class="actions"><span class="no">No</span><span class="yes">Yes</span></div></div>
</section>

<!-- Paper mode -->
<section class="phone" style="left:702px;top:612px">
  <div class="status"><span class="carrier">●●●●● Kestrel</span><span class="time">9:41 AM</span><span class="battery">100%<i class="batt"></i></span></div>
  <div class="navbar">PAPER</div>
  <div class="stats"><div class="stat dark"><b>107</b><small>Remain</small></div><div class="stat red"><b>2</b><small>Wrong</small></div><div class="stat teal"><b>10</b><small>Correct</small></div></div>
  <div class="prompt short"><div class="word" style="margin-top:6px">loose</div><div class="reading jp" style="font-size:7px">マン</div><svg class="fav" width="15" height="15"><use href="#i-star"/></svg></div>
  <div class="canvas-area"><div class="v"></div><div class="h"></div><div class="guide">漫</div></div>
  <nav class="tabbar">
    <div class="tab"><svg><use href="#i-home"/></svg>Home</div>
    <div class="tab"><svg><use href="#i-gear"/></svg>Settings</div>
    <div class="tab"><svg><use href="#i-search"/></svg>Search</div>
    <div class="tab"><svg><use href="#i-grid"/></svg>Game</div>
    <div class="tab on"><svg><use href="#i-paper"/></svg>Paper</div>
  </nav>
</section>

<div class="brand">Moriva<br>Tutor</div>

</body>
</html>
```